Altamira Business Card Design

The name of the business is Ruben Altamira, CPA LLC
The service that we offer is Accounting, Tax & Consulting Services. I need it to have the following items:
Ruben Altamira, Principal
Phone Number
Email Address
Physical Address

I have attached the company logo, one in black and one in white. Please provide a design in black background and the other in white background. Please include "Accounting, Tax & Consulting Services". I want the business card to be clean and very professional.

```html
<!DOCTYPE html>
<html lang="en">
<head>
<meta charset="utf-8">
<title>Ruben Altamira, CPA LLC — Business Card</title>
<link href="https://fonts.googleapis.com/css2?family=Montserrat:wght@500;600;700&family=Roboto:wght@300;400&display=swap" rel="stylesheet">
<style>
  :root {
    --backdrop: #2c2c2d;
    --card: #262628;
    --card-light: #f3f3f1;
    --ink: #1d1d1f;
    --red: #a61e23;
    --white: #f2f2f2;
    --grey: #b9b9bb;
    --grey-dark: #6a6a6d;
    --text: #e0e0e0;
    --rule: #9a9a9c;
  }
  * { margin: 0; padding: 0; box-sizing: border-box; }
  html, body { width: 1200px; height: 1138px; overflow: hidden; }
  body { background: var(--backdrop); position: relative; font-family: "Roboto", Arial, sans-serif; }

  .card { position: absolute; border-radius: 16px; }
  .card-front { left: 273px; top: 184px; width: 621px; height: 376px; background: var(--card-light); }
  .card-back  { left: 274px; top: 606px; width: 619px; height: 375px; background: var(--card); }

  .front-identity {
    position: absolute; left: 0; right: 0; top: 140px;
    text-align: center;
  }
  .front-square { width: 40px; height: 40px; background: var(--ink); margin: 0 auto 22px; }
  .front-name {
    font-family: "Montserrat", Arial, sans-serif; font-weight: 700;
    font-size: 30px; letter-spacing: 1px; color: var(--ink); line-height: 1;
  }
  .front-services {
    font-family: "Montserrat", Arial, sans-serif; font-weight: 500;
    font-size: 15px; letter-spacing: 2px; color: var(--red); margin-top: 14px;
    text-transform: uppercase;
  }

  .brand { position: absolute; left: 28px; top: 40px; display: flex; align-items: center; }
  .brand-square { width: 56px; height: 56px; background: var(--white); margin-right: 16px; }
  .brand-name {
    font-family: "Montserrat", Arial, sans-serif; font-weight: 600;
    font-size: 25px; color: var(--white); line-height: 1; letter-spacing: 0.3px;
  }
  .brand-tagline {
    font-family: "Montserrat", Arial, sans-serif; font-weight: 500;
    font-size: 17.5px; color: var(--grey); letter-spacing: 2.2px; margin-top: 8px;
  }

  .services {
    position: absolute; left: 28px; top: 128px;
    font-weight: 300; font-size: 15px; letter-spacing: 0.6px; color: var(--grey);
  }

  .person { position: absolute; left: 28px; top: 210px; }
  .person-name {
    font-family: "Montserrat", Arial, sans-serif; font-weight: 700;
    font-size: 21px; color: var(--red); letter-spacing: 0.4px; line-height: 1.1;
  }
  .person-title { font-size: 16.5px; color: var(--text); margin-top: 3px; }

  .divider { position: absolute; left: 28px; top: 248px; }

  .address {
    position: absolute; left: 28px; top: 300px;
    font-weight: 300; font-size: 16.5px; line-height: 24px; color: var(--text);
  }

  .contacts { position: absolute; right: 32px; top: 278px; list-style: none; }
  .contacts li {
    display: flex; align-items: center; justify-content: flex-end;
    font-weight: 300; font-size: 16.5px; line-height: 24px; color: var(--text);
  }
  .contacts svg { margin-left: 12px; fill: var(--red); }
</style>
</head>
<body>
  <section class="card card-front">
    <div class="front-identity">
      <div class="front-square"></div>
      <p class="front-name">RUBEN ALTAMIRA, CPA LLC</p>
      <p class="front-services">Accounting, Tax &amp; Consulting Services</p>
    </div>
  </section>

  <section class="card card-back">
    <div class="brand">
      <div class="brand-square"></div>
      <div>
        <p class="brand-name">RUBEN ALTAMIRA, CPA LLC</p>
        <p class="brand-tagline">CERTIFIED PUBLIC ACCOUNTANT</p>
      </div>
    </div>

    <p class="services">Accounting, Tax &amp; Consulting Services</p>

    <div class="person">
      <p class="person-name">RUBEN ALTAMIRA</p>
      <p class="person-title">Principal</p>
    </div>

    <svg class="divider" width="564" height="40" viewBox="0 0 564 40">
      <path d="M0 28 H286 C330 28 322 4 370 4 H562" fill="none" stroke="var(--rule)" stroke-width="2"/>
    </svg>

    <p class="address">4821, Larkspur Avenue, Brook<br>Valley, US 288014</p>

    <ul class="contacts">
      <li>828-555-0147
        <svg width="14" height="14" viewBox="0 0 14 14"><path d="M1 4c0-2 2-3 6-3s6 1 6 3v1H10V3.5H4V5H1zM3 6h8l2 6H1z"/></svg>
      </li>
      <li>ra@rubenaltamirallc.com
        <svg width="14" height="14" viewBox="0 0 14 14"><rect x="0.5" y="3" width="13" height="9" rx="1.5"/></svg>
      </li>
      <li>www.rubenaltamirallc.com
        <svg width="14" height="14" viewBox="0 0 14 14"><circle cx="7" cy="7" r="6"/></svg>
      </li>
    </ul>
  </section>
</body>
</html>
```